Communications Consultancy needs Print Design Project

We are a communications consultancy providing training and services for organisations and individuals.

We have developed a Project Communication Strategy Model that is sound in functionality but poor in graphical design and structure.

We need to create a single page document that is a practical and profession tool to guide Project Managers through the process of communicating project outcomes.

The model will be used as a hard copy resource and will also need to be replicated onto a PowerPoint slide for instructional purposes.

Target Market(s)

Project Management Professionals

Industry/Entity Type

Communications

Requirements
Must have
• Icons to represent the different communication mediums (icons shown in attachment are just for example)

Enable future editing and be transfereable to PowerPoint

Have the company Logo (this can be privided as vector file etc.

Company contact details, website, phone, ABN etc.

```html
<!DOCTYPE html>
<html lang="en">
<head>
<meta charset="utf-8">
<title>Project Communication Strategy Model</title>
<link href="https://fonts.googleapis.com/css2?family=Open+Sans:wght@400;600;700&display=swap" rel="stylesheet">
<style>
  :root {
    --green: #8fbc3b;
    --dark: #2d2d2d;
    --footer: #231f20;
    --grid: #8a8a8a;
    --cell: #f0f0f2;
    --ink: #222;
    --white: #fff;
  }
  * { box-sizing: border-box; margin: 0; padding: 0; }
  html, body { width: 1200px; height: 848px; overflow: hidden; background: var(--white); }
  body { font-family: "Open Sans", Arial, sans-serif; color: var(--ink); }
  .sheet { position: relative; width: 1200px; height: 848px; }
  .abs { position: absolute; }

  .title { left: 31px; top: 50px; font-size: 24px; font-weight: 400; letter-spacing: 0.2px; }

  .brand { right: 33px; top: 54px; font-size: 26px; font-weight: 400; color: var(--ink); line-height: 1; white-space: nowrap; }

  .connectors { left: 0; top: 0; width: 1200px; height: 848px; }

  .node {
    background: var(--dark); color: var(--white); border-radius: 4px;
    display: flex; align-items: center; justify-content: center; font-size: 15px;
  }
  .node-event { left: 494px; top: 117px; width: 203px; height: 38px; font-size: 18px; }
  .node-yes { left: 416px; top: 211px; width: 80px; height: 40px; }
  .node-no { left: 678px; top: 211px; width: 80px; height: 40px; }
  .node-end { left: 839px; top: 211px; width: 80px; height: 40px; }
  .question { left: 540px; top: 172px; width: 112px; text-align: center; font-size: 13px; font-weight: 600; }

  .bar {
    background: var(--green); color: var(--ink); border-radius: 5px;
    display: flex; align-items: center; justify-content: center; font-size: 19px;
  }
  .bar-channel { left: 28px; top: 282px; width: 226px; height: 39px; }
  .bar-medium { left: 289px; top: 282px; width: 485px; height: 39px; }
  .bar-delivery { left: 804px; top: 282px; width: 363px; height: 39px; }
  .bar-sub { top: 341px; height: 30px; font-size: 14px; font-weight: 600; }
  .bar-technique { left: 802px; width: 201px; }
  .bar-priority { left: 1046px; width: 121px; }

  .col-labels { top: 362px; height: 30px; display: flex; }
  .col-labels span { display: block; font-size: 9px; transform: rotate(-14deg); transform-origin: left bottom; white-space: nowrap; padding-top: 14px; }
  .medium-labels { left: 316px; width: 485px; }
  .medium-labels span { width: 80.8px; }

  .grid { border-collapse: collapse; table-layout: fixed; }
  .grid th, .grid td { border: 1px solid var(--grid); }
  .grid th { background: var(--white); height: 27px; font-weight: 700; font-size: 7px; }
  .grid tr.shade td { background: var(--cell); }
  .grid td { height: 95px; }
  .medium-grid { left: 289px; top: 393px; width: 485px; }
  .medium-grid th svg { display: block; margin: 0 auto; }
  .technique-grid { left: 804px; top: 393px; width: 202px; }
  .priority-grid { left: 1046px; top: 393px; width: 121px; }
  .technique-grid th, .priority-grid th { border-left-color: #ccc; border-right-color: #ccc; }
  .technique-grid td, .priority-grid td { border-left-color: #ccc; border-right-color: #ccc; }

  .channel { left: 31px; width: 227px; height: 94px; border: 1px solid var(--green); border-radius: 3px; background: var(--white); }
  .channel-1 { top: 421px; }
  .channel-2 { top: 515px; }
  .channel-3 { top: 610px; }
  .channel-icon { position: absolute; left: 18px; top: 10px; }
  .channel-name { position: absolute; left: 0; width: 88px; bottom: 6px; text-align: center; font-size: 9px; font-weight: 700; }
  .channel-list { position: absolute; left: 96px; top: 6px; list-style: none; }
  .channel-list li { font-size: 8px; font-weight: 700; height: 17.6px; line-height: 14px; width: 120px; display: flex; }
  .channel-list li::after { content: ""; flex: 1; border-bottom: 1.5px dotted var(--ink); margin: 0 0 5px 2px; }

  .stages { left: 0; top: 731px; width: 1200px; height: 46px; }
  .stage { top: 742px; font-size: 19px; text-align: center; width: 200px; }
  .stage-who { left: 42px; }
  .stage-what { left: 430px; }
  .stage-how { left: 806px; }
  .stage-when { left: 1007px; }

  .footer {
    left: 0; top: 779px; width: 1200px; height: 69px; background: var(--footer);
    color: var(--white); font-size: 14px; padding: 26px 0 0 31px;
  }
</style>
</head>
<body>
<main class="sheet">
  <h1 class="abs title">Project&nbsp; Communication Strategy Model</h1>

  <div class="abs brand">Brightline Communications</div>

  <svg class="abs connectors" viewBox="0 0 1200 848" aria-hidden="true">
    <g stroke="var(--green)" stroke-width="7" fill="none">
      <line x1="596" y1="155" x2="596" y2="210"/>
      <polyline points="841,231 138,231 138,402"/>
    </g>
    <polygon points="128,400 148,400 138,416" fill="var(--green)"/>
    <rect x="578" y="213" width="36" height="36" rx="4" transform="rotate(45 596 231)" fill="var(--dark)"/>
  </svg>

  <div class="abs node node-event">Event</div>
  <div class="abs question">Reportable?</div>
  <div class="abs node node-yes">Yes</div>
  <div class="abs node node-no">No</div>
  <div class="abs node node-end">End</div>

  <div class="abs bar bar-channel">Channel</div>
  <div class="abs bar bar-medium">Medium</div>
  <div class="abs bar bar-delivery">Delivery</div>
  <div class="abs bar bar-sub bar-technique">Influencing Technique</div>
  <div class="abs bar bar-sub bar-priority">Priority</div>

  <div class="abs col-labels medium-labels">
    <span>Email</span><span>Phone</span><span>Meeting</span><span>System</span><span>Report</span><span>Presentation</span>
  </div>

  <table class="abs grid medium-grid">
    <thead>
      <tr>
        <th><svg width="20" height="14" viewBox="0 0 20 14"><rect x="1" y="1" width="18" height="12" fill="none" stroke="#222" stroke-width="1.6"/><polyline points="1,1 10,8 19,1" fill="none" stroke="#222" stroke-width="1.6"/></svg></th>
        <th><svg width="14" height="14" viewBox="0 0 14 14"><path d="M3 1 L5.5 1 L6.5 4.5 L4.8 5.8 Q6 8.5 8.2 9.2 L9.5 7.5 L13 8.5 L13 11 Q12 13 9.5 12.8 Q2 11 1.2 3.5 Q1.2 1.5 3 1 Z" fill="#222"/></svg></th>
        <th><svg width="22" height="14" viewBox="0 0 22 14"><circle cx="6" cy="4" r="2.6" fill="#222"/><circle cx="16" cy="4" r="2.6" fill="#222"/><circle cx="11" cy="5" r="3" fill="#222"/><path d="M1 13 Q1 7.5 6 7.5 Q9 7.5 10 10 L10 13Z M21 13 Q21 7.5 16 7.5 Q13 7.5 12 10 L12 13Z" fill="#222"/><path d="M6 13.5 Q6 8.5 11 8.5 Q16 8.5 16 13.5Z" fill="#222"/></svg></th>
        <th><svg width="18" height="15" viewBox="0 0 18 15"><rect x="1" y="1" width="16" height="13" fill="none" stroke="#222" stroke-width="1.6"/><rect x="4" y="4" width="4" height="4" fill="#222"/><rect x="10" y="4" width="4" height="2" fill="#222"/><rect x="10" y="8" width="4" height="3" fill="#222"/><rect x="4" y="10" width="4" height="1.5" fill="#222"/></svg></th>
        <th><svg width="20" height="14" viewBox="0 0 20 14"><path d="M1 2 L7 2 L9 4 L17 4 L17 6 L4 6 L1 13Z" fill="#222"/><path d="M4.5 7 L19 7 L16 13 L1.5 13Z" fill="#222"/></svg></th>
        <th><svg width="20" height="15" viewBox="0 0 20 15"><rect x="3" y="1" width="14" height="10" fill="none" stroke="#222" stroke-width="1.6"/><rect x="1" y="12" width="18" height="2" fill="#222"/></svg></th>
      </tr>
    </thead>
    <tbody>
      <tr class="shade"><td></td><td></td><td></td><td></td><td></td><td></td></tr>
      <tr><td></td><td></td><td></td><td></td><td></td><td></td></tr>
      <tr class="shade"><td></td><td></td><td></td><td></td><td></td><td></td></tr>
    </tbody>
  </table>

  <table class="abs grid technique-grid">
    <thead><tr><th>Rational</th><th>Emotional</th><th>Consultation</th><th>Collaboration</th></tr></thead>
    <tbody>
      <tr class="shade"><td></td><td></td><td></td><td></td></tr>
      <tr><td></td><td></td><td></td><td></td></tr>
      <tr class="shade"><td></td><td></td><td></td><td></td></tr>
    </tbody>
  </table>

  <table class="abs grid priority-grid">
    <thead><tr><th>High</th><th>Medium</th><th>Low</th></tr></thead>
    <tbody>
      <tr class="shade"><td></td><td></td><td></td></tr>
      <tr><td></td><td></td><td></td></tr>
      <tr class="shade"><td></td><td></td><td></td></tr>
    </tbody>
  </table>

  <section class="abs channel channel-1">
    <svg class="channel-icon" width="52" height="56" viewBox="0 0 52 56"><polygon points="26,2 50,28 36,28 36,54 16,54 16,28 2,28" fill="none" stroke="var(--green)" stroke-width="1.6"/></svg>
    <div class="channel-name">Management</div>
    <ol class="channel-list"><li>1)</li><li>2)</li><li>3)</li><li>4)</li><li>5)</li></ol>
  </section>
  <section class="abs channel channel-2">
    <svg class="channel-icon" width="56" height="52" viewBox="0 0 56 52"><polygon points="54,26 28,50 28,36 2,36 2,16 28,16 28,2" fill="none" stroke="var(--green)" stroke-width="1.6"/></svg>
    <div class="channel-name">Stakeholders</div>
    <ol class="channel-list"><li>1)</li><li>2)</li><li>3)</li><li>4)</li><li>5)</li></ol>
  </section>
  <section class="abs channel channel-3">
    <svg class="channel-icon" width="52" height="56" viewBox="0 0 52 56"><polygon points="26,54 50,28 36,28 36,2 16,2 16,28 2,28" fill="none" stroke="var(--green)" stroke-width="1.6"/></svg>
    <div class="channel-name">Project Team</div>
    <ol class="channel-list"><li>1)</li><li>2)</li><li>3)</li><li>4)</li><li>5)</li></ol>
  </section>

  <svg class="abs stages" viewBox="0 731 1200 46" aria-hidden="true">
    <g fill="var(--white)" stroke="var(--green)" stroke-width="1.6">
      <polygon points="1,733 270,733 284,754 270,775 1,775"/>
      <polygon points="272,733 778,733 792,754 778,775 272,775 286,754"/>
      <polygon points="782,733 1028,733 1042,754 1028,775 782,775 796,754"/>
      <polygon points="1032,733 1199,733 1199,775 1032,775 1046,754"/>
    </g>
  </svg>
  <div class="abs stage stage-who">Who</div>
  <div class="abs stage stage-what">What</div>
  <div class="abs stage stage-how">How</div>
  <div class="abs stage stage-when">When</div>

  <footer class="abs footer">Brightline Communications Pty. Ltd / www.brightlinecomms.example / PO Box 410, Harbourview NSW 2000 / +61 2 5550 0134&nbsp; ABN: 00 000 000 000</footer>
</main>
</body>
</html>
```